Jewelers Website

This is for the DESIGN ONLY.
I am a software programmer and will be doing the development.
New website design for
www.lumaoakstones.com.au
Need a fresh new look for an online only jewellery business who produce their jewellery by hand. I would like it designed in a parallax style. Feel free to recommend fonts to use for the site. This is an Australian based company located in NSW so shots of sites in NSW might make nice background images.
http://brixolatemplates.net/demo/#theme=parallax
To contain the below sections
About Us
Contact Us
Gallery
Testimonials
Diamond Types
The colour scheme is to be Black / White and Silver.
With the Parallax style there will be moving sections and images for added impact.
Target Market(s)
Young Adults mainly engagement jewellery
Industry/Entity Type
Software
Look and feel

```html
<!DOCTYPE html>
<html lang="en">
<head>
<meta charset="utf-8">
<title>Luma Oak Stones — Handmade Jewellery</title>
<link rel="stylesheet" href="https://fonts.googleapis.com/css2?family=Open+Sans:wght@300;400;600&display=swap">
<style>
:root{
  --charcoal:#232323;
  --footer:#3a3a3a;
  --white:#ffffff;
  --silver:#c9c9c9;
  --mist:#ececec;
  --text:#555555;
  --field-line:#cfcfcf;
  --button:#444444;
  --frame:#7a7a7a;
}
*{margin:0;padding:0;box-sizing:border-box}
html,body{width:1200px;height:3404px;overflow:hidden}
body{font-family:"Open Sans",Arial,sans-serif;color:var(--text);background:var(--white);position:relative}
section,header,footer{position:absolute;left:0;width:1200px;overflow:hidden}
.abs{position:absolute}
.fill{inset:0}

/* header */
.site-header{top:0;height:163px;background:linear-gradient(180deg,#2c2c2c,#1c1c1c)}
.brand{left:89px;top:46px;color:var(--white);font-weight:400;font-size:31px;line-height:33px;letter-spacing:1px;text-transform:uppercase}
.main-nav{right:89px;top:86px;display:flex;gap:34px}
.main-nav a{color:var(--white);text-decoration:none;font-size:16px}

/* hero */
.hero{top:163px;height:558px;background:#111}
.hero-photo{background:
  radial-gradient(ellipse 520px 300px at 30% 48%,rgba(235,235,235,.95) 0%,rgba(170,170,170,.75) 30%,rgba(80,80,80,.4) 60%,rgba(0,0,0,0) 80%),
  radial-gradient(ellipse 300px 220px at 62% 30%,rgba(200,200,200,.7) 0%,rgba(90,90,90,.3) 55%,rgba(0,0,0,0) 80%),
  radial-gradient(ellipse 260px 200px at 88% 60%,rgba(190,190,190,.55) 0%,rgba(0,0,0,0) 75%),
  linear-gradient(180deg,#3a3a3a 0%,#242424 50%,#0c0c0c 100%)}
.hero-badge{left:841px;top:118px;width:264px;height:264px;border-radius:50%;background:rgba(0,0,0,.62);text-align:center;color:var(--white)}
.hero-badge .kicker{margin-top:52px;font-size:40px;font-weight:300;letter-spacing:2px;line-height:48px}
.hero-badge .sub{font-size:26px;font-weight:300;margin-top:10px;line-height:32px}
.hero-badge .cta{font-size:14px;margin-top:18px;display:flex;justify-content:center;align-items:center;gap:10px}
.hero-badge .cta i{width:15px;height:15px;border-radius:50%;background:var(--white);display:inline-block}
.dots{display:flex;gap:5px}
.dots span{width:18px;height:18px;border-radius:50%;background:#bbb;border:2px solid #888}
.dots span.on{background:var(--white)}
.hero .dots{left:558px;top:510px}

/* section heading */
.section-title{left:0;width:1200px;text-align:center;font-weight:300;font-size:40px;letter-spacing:1px;line-height:50px}
.title-rule{left:515px;width:170px;height:14px}
.dark .section-title{color:var(--white)}
.light .section-title{color:#444}

/* about */
.about{top:721px;height:469px;background:var(--white)}
.about .section-title{top:50px}
.about .title-rule{top:108px}
.ring-photo{left:89px;top:148px;width:357px;height:232px;background:
  radial-gradient(ellipse 110px 70px at 48% 46%,#f4f4f4 0%,#c4c4c4 45%,rgba(160,160,160,.0) 100%),
  radial-gradient(ellipse 170px 85px at 45% 50%,#9a9a9a 0%,#d2d2d2 55%,rgba(255,255,255,0) 100%),
  radial-gradient(ellipse 170px 60px at 50% 86%,#dedede 0%,rgba(255,255,255,0) 100%),#fff}
.about-copy{left:500px;top:176px;width:616px;font-size:13.5px;line-height:25px;color:#666}
.about-copy p+p{margin-top:10px}

/* gallery */
.gallery{top:1190px;height:537px;background:
  linear-gradient(180deg,rgba(60,60,60,.0) 0%,rgba(0,0,0,.35) 100%),
  linear-gradient(90deg,#262626 0%,#454545 25%,#2b2b2b 45%,#505050 75%,#2a2a2a 100%)}
.gallery .section-title{top:68px}
.gallery .title-rule{top:126px}
.gallery-grid{left:100px;top:180px;width:1000px;height:310px}

/* testimonials */
.testimonials{top:1727px;height:472px;background:linear-gradient(180deg,#e2e2e2 0%,#f3f3f3 45%,#e6e6e6 100%)}
.testimonials h2{top:52px;width:1200px;text-align:center;font-weight:400;font-size:34px;color:#222;line-height:44px}
.avatar{left:524px;top:122px;width:144px;height:144px;border-radius:50%;border:5px solid var(--white);background:radial-gradient(circle at 50% 45%,#e9d3c2 0%,#c7b09e 55%,#f2f2f2 80%);box-shadow:0 2px 6px rgba(0,0,0,.2)}
.quote{top:296px;width:1200px;text-align:center;font-size:18px;line-height:34px;color:#555}
.quote-author{right:143px;top:368px;font-size:16px;color:#555}
.testimonials .dots{left:560px;top:413px}
.testimonials .dots span{width:14px;height:14px}

/* jewelry types */
.types{top:2199px;height:540px;background:
  radial-gradient(ellipse 600px 260px at 50% 75%,rgba(110,110,110,.5) 0%,rgba(0,0,0,0) 80%),
  linear-gradient(180deg,#4a4a4a 0%,#2e2e2e 45%,#1c1c1c 100%)}
.types .section-title{top:70px;font-size:36px}
.types .title-rule{top:120px;left:435px;width:330px}
.type-card{top:234px;width:294px;height:204px;border:7px solid var(--frame)}
.type-card.one{left:89px;background:
  radial-gradient(ellipse 60px 50px at 50% 50%,#7fd6ea 0%,#2f9fbc 55%,rgba(47,159,188,0) 100%),
  radial-gradient(ellipse 140px 80px at 50% 52%,#e6e6e6 0%,#9a9a9a 60%,#cfd3d4 100%)}
.type-card.two{left:448px;background:
  radial-gradient(ellipse 95px 70px at 52% 55%,#f4f4f4 0%,#b5b5b5 40%,#4a4a4a 75%,#080808 100%)}
.type-card.three{left:815px;background:
  radial-gradient(ellipse 55px 40px at 30% 55%,#e0e0e0 0%,rgba(0,0,0,0) 100%),
  radial-gradient(ellipse 60px 45px at 72% 48%,#ececec 0%,rgba(0,0,0,0) 100%),
  linear-gradient(180deg,#1a1a1a,#050505)}

/* contact */
.contact{top:2739px;height:548px;background:var(--white)}
.contact .section-title{top:50px}
.contact .title-rule{top:108px}
.field{left:138px;width:445px;border:1.5px solid var(--field-line);font-size:14px;color:#555;padding:0 14px}
.field.name{top:171px;height:46px;line-height:43px}
.field.email{top:237px;height:48px;line-height:45px}
.field.message{top:306px;height:109px;padding-top:12px}
.send{left:474px;top:443px;width:109px;height:49px;background:var(--button);color:var(--white);text-align:center;line-height:49px;font-size:17px;letter-spacing:1px}
.map{left:683px;top:171px;width:402px;height:163px;border:1px solid #d8d8d8;background:
  radial-gradient(ellipse 60px 40px at 18% 40%,#b9d3ec 0%,rgba(185,211,236,0) 100%),
  radial-gradient(ellipse 120px 70px at 70% 45%,#f1e2b5 0%,rgba(241,226,181,0) 100%),
  radial-gradient(ellipse 90px 50px at 60% 85%,#cfe3c0 0%,rgba(207,227,192,0) 100%),
  #eceae4}
.contact-item{font-size:14px;line-height:26px;color:#555;display:flex;gap:14px}
.contact-item svg{flex:none;margin-top:4px}
.address{left:683px;top:382px}
.mail{left:918px;top:382px}
.phone{left:918px;top:428px}

/* footer */
.site-footer{top:3287px;height:117px;background:var(--footer);color:var(--white)}
.footer-links{left:89px;top:30px;font-size:14px}
.copyright{left:89px;top:68px;font-size:14px}
.social{left:910px;top:30px;display:flex;gap:16px}
.social span{width:34px;height:34px;display:block}
.social .s1{background:#3b5998}.social .s2{background:#2fa9e0}.social .s3{background:#f26522}.social .s4{background:#e52d27}
</style>
</head>
<body>

<header class="site-header">
  <div class="abs brand">Luma Oak<br>Stones</div>
  <nav class="abs main-nav">
    <a href="#about">About Us</a><a href="#gallery">Gallery</a><a href="#testimonials">Testimonials</a><a href="#types">Diamond Types</a><a href="#contact">Contact Us</a>
  </nav>
</header>

<section class="hero dark">
  <div class="abs fill hero-photo" role="img" aria-label="Loose brilliant-cut diamonds scattered on dark velvet"></div>
  <div class="abs hero-badge">
    <div class="kicker">JEWELRY</div>
    <div class="sub">NEW COLLECTIONS</div>
    <div class="cta"><i></i>ENTER SHOP</div>
  </div>
  <div class="abs dots"><span class="on"></span><span></span><span></span><span></span></div>
</section>

<section class="about light" id="about">
  <h2 class="abs section-title">ABOUT US</h2>
  <svg class="abs title-rule" viewBox="0 0 170 14"><line x1="0" y1="7" x2="170" y2="7" stroke="#555" stroke-width="1"/><rect x="80" y="2" width="10" height="10" transform="rotate(45 85 7)" fill="#222"/></svg>
  <div class="abs ring-photo" role="img" aria-label="Halo diamond engagement ring on white"></div>
  <div class="abs about-copy">
    <p>Duis autem vel eum iriure dolor in hendrerit in vulputate velit esse molestie consequat, vel illum dolore eu feugiat nulla facilisis at vero eros et accumsan et iusto odio dignissim qui blandit praesent luptatum zzril delenit augue duis dolore te feugait nulla facilisi. Nam liber tempor cum soluta nobis eleifend option congue nihil imperdiet doming id quod mazim placerat facer possim assum. Typi non habent claritatem insitam; est usus legentis in iis qui facit eorum claritatem.</p>
    <p>Claritas est etiam processus dynamicus, qui sequitur mutationem consuetudium lectorum. Mirum est notare quam littera gothica, quam nunc putamus parum claram, anteposuerit litterarum formas humanitatis per seacula quarta decima et quinta decima. Eodem modo typi.</p>
  </div>
</section>

<section class="gallery dark" id="gallery" role="img" aria-label="City skyline at dusk in black and white behind the gallery">
  <h2 class="abs section-title">GALLERY</h2>
  <svg class="abs title-rule" viewBox="0 0 170 14"><line x1="0" y1="7" x2="170" y2="7" stroke="#ddd" stroke-width="1"/><rect x="80" y="2" width="10" height="10" transform="rotate(45 85 7)" fill="#fff"/></svg>
  <svg class="abs gallery-grid" viewBox="0 0 1000 310" role="img" aria-label="Gallery of diamond and jewellery photographs set in diamond-shaped tiles">
    <defs>
      <radialGradient id="tileA" cx=".5" cy=".5" r=".7"><stop offset="0" stop-color="#ffffff"/><stop offset=".5" stop-color="#b8b8b8"/><stop offset="1" stop-color="#5a5a5a"/></radialGradient>
      <radialGradient id="tileB" cx=".5" cy=".5" r=".7"><stop offset="0" stop-color="#e6e6e6"/><stop offset=".6" stop-color="#8a8a8a"/><stop offset="1" stop-color="#3a3a3a"/></radialGradient>
      <radialGradient id="tileC" cx=".5" cy=".5" r=".7"><stop offset="0" stop-color="#f2f2f2"/><stop offset=".45" stop-color="#4a4a4a"/><stop offset="1" stop-color="#0a0a0a"/></radialGradient>
    </defs>
    <g stroke="#fff" stroke-width="3">
      <rect x="-66" y="-66" width="132" height="132" transform="translate(211 100) rotate(45)" fill="url(#tileA)"/>
      <rect x="-66" y="-66" width="132" height="132" transform="translate(405 100) rotate(45)" fill="url(#tileB)"/>
      <rect x="-66" y="-66" width="132" height="132" transform="translate(601 100) rotate(45)" fill="url(#tileA)"/>
      <rect x="-66" y="-66" width="132" height="132" transform="translate(797 100) rotate(45)" fill="url(#tileB)"/>
      <rect x="-66" y="-66" width="132" height="132" transform="translate(66 205) rotate(45)" fill="url(#tileB)"/>
      <rect x="-48" y="-48" width="96" height="96" transform="translate(300 220) rotate(45)" fill="url(#tileA)"/>
      <rect x="-66" y="-66" width="132" height="132" transform="translate(500 205) rotate(45)" fill="url(#tileA)"/>
      <rect x="-66" y="-66" width="132" height="132" transform="translate(700 205) rotate(45)" fill="url(#tileB)"/>
      <rect x="-66" y="-66" width="132" height="132" transform="translate(906 205) rotate(45)" fill="url(#tileC)"/>
    </g>
  </svg>
</section>

<section class="testimonials" id="testimonials">
  <h2 class="abs">Loved by thousands of people world wide</h2>
  <div class="abs avatar" role="img" aria-label="Customer portrait"></div>
  <p class="abs quote">I am so happy to have met you! Before Vocal Reset, I had vocal<br>problems that clouded my mind and made it zero fun to sing. Now I sing again and even have a weekly job as a speaker.</p>
  <div class="abs quote-author">- Jonas, Germany</div>
  <div class="abs dots"><span class="on"></span><span></span><span></span><span></span></div>
</section>

<section class="types dark" id="types" role="img" aria-label="Harbour city aerial view in black and white behind the jewellery types">
  <h2 class="abs section-title">EXQUISITE JEWELRY TYPES FOR YOU</h2>
  <svg class="abs title-rule" viewBox="0 0 330 14"><line x1="0" y1="7" x2="330" y2="7" stroke="#ddd" stroke-width="1"/><rect x="160" y="2" width="10" height="10" transform="rotate(45 165 7)" fill="#fff"/></svg>
  <div class="abs type-card one" role="img" aria-label="Aquamarine and diamond cocktail ring"></div>
  <div class="abs type-card two" role="img" aria-label="Pavé diamond band ring on black"></div>
  <div class="abs type-card three" role="img" aria-label="Pair of diamond engagement rings on black"></div>
</section>

<section class="contact light" id="contact">
  <h2 class="abs section-title">CONTACT US</h2>
  <svg class="abs title-rule" viewBox="0 0 170 14"><line x1="0" y1="7" x2="170" y2="7" stroke="#555" stroke-width="1"/><rect x="80" y="2" width="10" height="10" transform="rotate(45 85 7)" fill="#222"/></svg>
  <div class="abs field name">Name</div>
  <div class="abs field email">Email</div>
  <div class="abs field message">Send your message</div>
  <div class="abs send">SEND</div>
  <div class="abs map" role="img" aria-label="Street map showing the studio location"></div>
  <div class="abs contact-item address">
    <svg width="14" height="18" viewBox="0 0 14 18"><path d="M7 0C3 0 0 3 0 7c0 5 7 11 7 11s7-6 7-11c0-4-3-7-7-7z" fill="#444"/><circle cx="7" cy="7" r="2.5" fill="#fff"/></svg>
    <div>48 Harbour Lane,<br>Newcastle NSW 2300<br>Australia</div>
  </div>
  <div class="abs contact-item mail">
    <svg width="18" height="14" viewBox="0 0 18 14"><rect width="18" height="14" fill="#444"/><path d="M0 0l9 7 9-7" fill="none" stroke="#fff" stroke-width="1.5"/></svg>
    <div>hello@lumaoakstones.com.au</div>
  </div>
  <div class="abs contact-item phone">
    <svg width="16" height="16" viewBox="0 0 16 16"><path d="M3 0l3 4-2 2c1 2 4 5 6 6l2-2 4 3-2 3C7 16 0 9 0 3z" fill="#444"/></svg>
    <div>02 5550 1284</div>
  </div>
</section>

<footer class="site-footer">
  <div class="abs footer-links">Terms and Conditions | Privacy Promise | FAQ's | Contact Us</div>
  <div class="abs copyright">Copyright © 2013. All Rights Reserved.</div>
  <div class="abs social"><span class="s1"></span><span class="s2"></span><span class="s3"></span><span class="s4"></span></div>
</footer>

</body>
</html>
```